Corvane semiconductor corporate presentation

We need a new template with some fresh design elements as we've just announced the acquisition of a new company. Similarly, the backend of the ppt is not set up correctly - and doesn't format properly when dropping in copied text. Attached is the powerpoint presentation/ template as it stands today.
Industry/Entity Type
It Company
Font styles to use
Other font styles liked:
- Arial
Look and feel
Each slider illustrates characteristics of the customer's brand and the style your logo design should communicate.

```html
<!DOCTYPE html>
<html lang="en">
<head>
<meta charset="utf-8">
<title>Why Corvane?</title>
<link href="https://fonts.googleapis.com/css2?family=Lato:wght@300;400;700&display=swap" rel="stylesheet">
<style>
  :root {
    --brand-teal: #00a9ce;
    --title-teal: #1a9fc9;
    --badge-teal: #0e6f8a;
    --body-text: #3a3a3a;
    --rule-grey: #b8c2c8;
    --bg-white: #ffffff;
    --bg-mist: #d6e6f2;
    --on-brand: #ffffff;
  }
  * { margin: 0; padding: 0; box-sizing: border-box; }
  html, body { width: 1200px; height: 900px; overflow: hidden; background: var(--bg-white); }
  body { font-family: "Lato", Arial, sans-serif; }

  .slide { position: relative; width: 1200px; height: 900px; overflow: hidden; background: var(--bg-white); }

  .backdrop {
    position: absolute; inset: 0 0 82px 0;
    background: linear-gradient(100deg, var(--bg-white) 0%, var(--bg-white) 42%, #eaf2f8 62%, var(--bg-mist) 100%);
  }

  .slide-title {
    position: absolute; left: 20px; top: 18px;
    font-size: 45px; font-weight: 300; color: var(--title-teal); letter-spacing: 0.3px;
  }
  .title-rule { position: absolute; left: 0; top: 80px; }

  .points { position: absolute; left: 45px; top: 166px; list-style: none; }
  .point {
    display: flex; align-items: center; height: 44px; margin-bottom: 51.5px;
    font-size: 29.6px; color: var(--body-text); font-weight: 400; white-space: nowrap;
  }
  .point-marker {
    width: 30px; height: 30px; border-radius: 50%; background: var(--brand-teal);
    margin-right: 17px; flex: none;
  }

  .footer-rule { position: absolute; left: 0; top: 817px; width: 1200px; height: 2px; background: var(--rule-grey); }
  .footer {
    position: absolute; left: 0; top: 822px; width: 1200px; height: 78px;
    background: var(--brand-teal); color: var(--on-brand);
  }
  .footer-brand {
    position: absolute; left: 18px; top: 14px; display: flex; align-items: center;
    font-size: 40px; font-weight: 700; letter-spacing: -0.5px;
  }
  .footer-brand-mark { width: 30px; height: 30px; border-radius: 50%; background: var(--on-brand); margin-right: 10px; }
  .copyright {
    position: absolute; left: 0; width: 100%; top: 37px; text-align: center;
    font-size: 17px; font-weight: 400; padding-right: 8px;
  }
  .page-number {
    position: absolute; left: 1126px; top: 16px; width: 52px; height: 52px; border-radius: 50%;
    background: var(--badge-teal); display: flex; align-items: center; justify-content: center;
    font-size: 18px; font-weight: 700;
  }
</style>
</head>
<body>
<main class="slide">
  <div class="backdrop" role="img" aria-label="Soft pale-blue faceted polygon backdrop fading in from the right"></div>

  <h1 class="slide-title">Why Corvane?</h1>
  <svg class="title-rule" width="252" height="22" viewBox="0 0 252 22" aria-hidden="true">
    <line x1="0" y1="1" x2="250" y2="1" stroke="var(--title-teal)" stroke-width="2"/>
    <polygon points="202,1 248,1 225,20" fill="var(--title-teal)"/>
  </svg>

  <ul class="points">
    <li class="point"><span class="point-marker"></span>Leading power management ICs enabling lowest power system design</li>
    <li class="point"><span class="point-marker"></span>Leading Linkwave connectivity solutions for emerging IoT applications</li>
    <li class="point"><span class="point-marker"></span>Innovating New Technologies, RF wireless Charging and GaN power ICs</li>
    <li class="point"><span class="point-marker"></span>Operational excellence in high volume, fast product ramp for smartphones</li>
    <li class="point"><span class="point-marker"></span>Ecosystem PMIC partnerships with leading application processor vendors</li>
  </ul>

  <div class="footer-rule"></div>
  <footer class="footer">
    <div class="footer-brand"><span class="footer-brand-mark"></span>corvane</div>
    <p class="copyright">© 2017 Corvane Semiconductor</p>
    <div class="page-number">01</div>
  </footer>
</main>
</body>
</html>
```